Business Name is RT Glamworks - Make-up Artist

I'm looking for an attractive and eye catching business card for for mobile make-up artist business. On the front of the card, I just want the name RT Glamworks in feminine type cursive writing and underneath my name Tessa Rowan and Make-Up Artist.
On the back of the card, I would like written down one side the following;
Make-Up Tutorials
Bridal
Photography
Debutante
Formals
Family Portraits
I would also like the following details as well as the Chatterly and Picvault Icons;
Mobile: 0482 615 379
Email: tessarowan@mailbrook.net
Website: tessarowan.velmira.com
Certificate III in Make-Up
Also, I would like a section that says Your Next Appointment and a space to put that information.
I would also like the Velmira Symbol on the bottom right hand corner (I have attached)

Target Market(s)

Mostly females

Industry/Entity Type

Makeup

Contact Information for Business Card

RT Glamworks
Tessa Rowan - Make-Up Artist

Font styles to use
Script

Colors
b768aa
886aae
e34297

Requirements
Must have
• Mobile: 0482 615 379
• Email: tessarowan@mailbrook.net
• Website: tessarowan.velmira.com
• Certificate III in Make-Up
Nice to have
• Something to do with make-up like a smudged lipstick or some eye shadow
Should not have
• Don't want it too busy

```html
<!DOCTYPE html>
<html lang="en">
<head>
<meta charset="utf-8">
<title>RT Glamworks – Business Card</title>
<link href="https://fonts.googleapis.com/css2?family=Great+Vibes&family=Lobster&family=Open+Sans:wght@400&display=swap" rel="stylesheet">
<style>
  :root {
    --pink: #e4439a;
    --plum: #a2479c;
    --ornament: #b0399c;
    --lavender: #886aae;
    --ink: #111111;
    --paper: #ffffff;
    --stage-light: #c6c6c6;
    --stage-dark: #5c5c5c;
  }
  * { margin: 0; padding: 0; box-sizing: border-box; }
  html, body { width: 1200px; height: 1200px; overflow: hidden; }
  body {
    position: relative;
    background: radial-gradient(circle at 50% 50%, var(--stage-light) 0%, #9a9a9a 35%, var(--stage-dark) 75%);
    font-family: "Lobster", cursive;
  }
  .side-label {
    position: absolute;
    font-family: "Open Sans", sans-serif;
    font-size: 36px;
    color: var(--paper);
    line-height: 1;
  }
  .side-label--front { left: 192px; top: 80px; }
  .side-label--back { left: 819px; top: 678px; }

  .card {
    position: absolute;
    width: 732px;
    height: 418px;
    overflow: hidden;
  }
  .card--front { left: 29px; top: 149px; background: var(--paper); }
  .card--back { left: 455px; top: 765px; background: var(--pink); color: var(--paper); }

  .front-wave { position: absolute; left: 0; top: 0; width: 732px; height: 418px; }
  .ornament-band {
    position: absolute;
    left: 4px;
    width: 724px;
    height: 60px;
    border-radius: 30px;
    background: linear-gradient(90deg, #c03da0, var(--ornament) 50%, #c03da0);
    opacity: 0.75;
  }
  .card--front .ornament-band { top: 355px; }
  .card--back .ornament-band { top: 2px; height: 52px; }

  .brand-mark {
    position: absolute;
    left: 28px; top: 30px;
    font-family: "Great Vibes", cursive;
    font-size: 58px;
    color: var(--ink);
    line-height: 1;
  }
  .owner {
    position: absolute;
    right: 226px; top: 160px;
    text-align: right;
    color: var(--plum);
  }
  .owner__name { font-family: "Lobster", cursive; font-size: 54px; line-height: 1; }
  .owner__role { font-family: "Great Vibes", cursive; font-size: 30px; line-height: 1; margin-top: 2px; }

  .service {
    position: absolute;
    font-size: 27px;
    line-height: 1;
    white-space: nowrap;
  }
  .service::before {
    content: "";
    position: absolute;
    left: -20px; top: 50%;
    transform: translateY(-50%);
    border-left: 14px solid var(--lavender);
    border-top: 9px solid transparent;
    border-bottom: 9px solid transparent;
  }
  .appointment {
    position: absolute;
    left: 473px; top: 233px;
    font-size: 18px;
  }
  .appointment__line {
    position: absolute;
    left: 468px; top: 296px;
    width: 209px; height: 2px;
    background: var(--paper);
  }
  .contact {
    position: absolute;
    left: 34px;
    display: flex;
    align-items: center;
    gap: 7px;
    font-size: 18px;
    line-height: 1;
  }
  .contact svg { width: 18px; height: 18px; flex: none; }
  .partner {
    position: absolute;
    left: 604px; top: 348px;
    display: flex;
    align-items: center;
    gap: 8px;
    font-size: 22px;
    color: var(--paper);
  }
  .partner__square { width: 16px; height: 16px; background: var(--paper); }
</style>
</head>
<body>
  <div class="side-label side-label--front">Front</div>
  <div class="side-label side-label--back">Back</div>

  <section class="card card--front">
    <svg class="front-wave" viewBox="0 0 732 418" aria-hidden="true">
      <path d="M0 287 Q366 430 732 287 L732 418 L0 418 Z" fill="var(--pink)"/>
    </svg>
    <div class="ornament-band" role="img" aria-label="Decorative swirl flourish border"></div>
    <div class="brand-mark">RT Glamworks</div>
    <div class="owner">
      <div class="owner__name">Tessa Rowan</div>
      <div class="owner__role">Make-Up Artist</div>
    </div>
  </section>

  <section class="card card--back">
    <div class="ornament-band" role="img" aria-label="Decorative swirl flourish border"></div>

    <div class="service" style="left:62px; top:72px;">Make-Up Tutorials</div>
    <div class="service" style="left:62px; top:118px;">Bridal</div>
    <div class="service" style="left:62px; top:165px;">Photography</div>
    <div class="service" style="left:62px; top:232px;">Certificate III in Make-Up</div>

    <div class="service" style="left:473px; top:64px;">Debutante</div>
    <div class="service" style="left:473px; top:111px;">Formals</div>
    <div class="service" style="left:473px; top:157px;">Family Portraits</div>

    <div class="appointment">Your Next Appointment</div>
    <div class="appointment__line"></div>

    <div class="contact" style="top:301px;">
      <svg viewBox="0 0 20 20" aria-hidden="true"><circle cx="10" cy="10" r="8.5" fill="none" stroke="#fff" stroke-width="1.5"/><path d="M7 5.5l2 2-1 1.2c.6 1.3 1.5 2.2 2.8 2.8l1.2-1 2 2-1.2 1.4C9.8 13.6 6.4 10.2 5.6 7z" fill="#fff"/></svg>
      <span>0482 615 379</span>
    </div>
    <div class="contact" style="top:330px;">
      <svg viewBox="0 0 20 20" aria-hidden="true"><rect x="1.5" y="4.5" width="17" height="11" fill="#fff"/><path d="M1.5 4.5l8.5 6 8.5-6" fill="none" stroke="var(--pink)" stroke-width="1.3"/></svg>
      <span>tessarowan@mailbrook.net</span>
    </div>
    <div class="contact" style="top:360px;">
      <svg viewBox="0 0 20 20" aria-hidden="true"><g fill="none" stroke="#fff" stroke-width="1.4"><circle cx="10" cy="10" r="8.5"/><ellipse cx="10" cy="10" rx="3.8" ry="8.5"/><path d="M1.5 10h17M3 5.5h14M3 14.5h14"/></g></svg>
      <span>tessarowan.velmira.com</span>
    </div>

    <div class="partner"><span class="partner__square"></span><span>Velmira</span></div>
  </section>
</body>
</html>
```